Brightleaf listings ad 2014 15

I need a design for an advertisement in our Brightleaf Listings book telephone directory.
The directory runs for a 12 month period.

Our business offers 24 hour glass replacements to homes, shops and offices.
Our service is usually required by customers that require their glass replaced urgently
.
The ad is 1 of many in the directory offering the same service so we need to attract the customers attention quickly and easily and deliver our message - "24hr glass replacements to doors windows and shopfronts. Call now 9372 6148".

I want to keep the data in the attached ad but with a professional graphic presentation.

The ad size is 58mm high x 83mm wide, full colour.

Target Market(s)

Our customer is generally someone in need of an emergency repair. They aren't spending time shopping around for a product, they have a problem that they want fixed promptly and professionally.

Industry/Entity Type

Business

Font styles to use
Sans Serif

Colors
0255a3
f37022

Requirements
Must have
• "24HR" must stand out, this is a key aspect of our service. The ad needs to be clear and easy to read.

```html
<!DOCTYPE html>
<html lang="en">
<head>
<meta charset="utf-8">
<title>Steadfast Glass – Glass Repairs</title>
<link rel="stylesheet" href="https://fonts.googleapis.com/css2?family=Roboto+Condensed:wght@400&family=Open+Sans:wght@700&family=Nunito:wght@600&family=Arimo:wght@700&display=swap">
<style>
  :root {
    --brand-blue: #0f5f9f;
    --deep-blue: #0255a3;
    --sky-blue: #1b8fd7;
    --panel-white: #ffffff;
    --rule-grey: #a9a9a9;
    --copy-grey: #8a8a8a;
    --tick-grey: #7d7d7d;
  }
  html, body {
    margin: 0;
    padding: 0;
    overflow: hidden;
  }
  body {
    width: 1200px;
    height: 838px;
  }
  .ad {
    position: relative;
    width: 1200px;
    height: 838px;
    background: var(--brand-blue);
    overflow: hidden;
  }
  .headline {
    position: absolute;
    top: 14px;
    left: 0;
    width: 100%;
    margin: 0;
    text-align: center;
    font-family: "Roboto Condensed", "Arial Narrow", sans-serif;
    font-weight: 400;
    font-size: 132px;
    line-height: 150px;
    color: var(--panel-white);
    letter-spacing: 1px;
  }
  .panel {
    position: absolute;
    top: 177px;
    left: 8px;
    width: 1184px;
    height: 473px;
    background: var(--panel-white);
    border-top: 11px solid var(--rule-grey);
    border-bottom: 7px solid var(--rule-grey);
    box-sizing: border-box;
  }
  .premises {
    position: absolute;
    top: 28px;
    left: 0;
    width: 100%;
    margin: 0;
    text-align: center;
    font-family: "Open Sans", Arial, sans-serif;
    font-weight: 700;
    font-size: 64px;
    line-height: 80px;
    color: var(--deep-blue);
    letter-spacing: 1px;
  }
  .premises .divider {
    color: var(--rule-grey);
    font-weight: 400;
    padding: 0 10px;
  }
  .availability {
    position: absolute;
    top: 122px;
    left: 22px;
    width: 1140px;
    height: 84px;
    margin: 0;
    background: var(--sky-blue);
    text-align: center;
    font-family: "Nunito", Arial, sans-serif;
    font-weight: 600;
    font-size: 66px;
    line-height: 84px;
    color: var(--panel-white);
    letter-spacing: 3px;
  }
  .credentials {
    position: absolute;
    top: 248px;
    left: 110px;
    width: 1000px;
    margin: 0;
    padding: 0;
    list-style: none;
    display: grid;
    grid-template-columns: 512px 488px;
    row-gap: 12px;
  }
  .credentials li {
    display: flex;
    align-items: center;
    font-family: "Open Sans", Arial, sans-serif;
    font-weight: 700;
    font-size: 34px;
    line-height: 48px;
    color: var(--copy-grey);
    letter-spacing: 0.5px;
  }
  .credentials .tick {
    width: 40px;
    height: 36px;
    margin-right: 18px;
    flex: none;
  }
  .brand-name {
    position: absolute;
    top: 374px;
    left: 0;
    width: 100%;
    margin: 0;
    text-align: center;
    font-family: "Open Sans", Arial, sans-serif;
    font-weight: 700;
    font-size: 72px;
    line-height: 90px;
    color: var(--deep-blue);
  }
  .call-to-action {
    position: absolute;
    top: 668px;
    left: 0;
    width: 100%;
    margin: 0;
    text-align: center;
    font-family: "Arimo", Arial, sans-serif;
    font-weight: 700;
    font-size: 118px;
    line-height: 150px;
    color: var(--panel-white);
    letter-spacing: 2px;
  }
</style>
</head>
<body>
  <main class="ad">
    <h1 class="headline">GLASS REPAIRS</h1>

    <section class="panel">
      <p class="premises">HOME<span class="divider">|</span>SHOP<span class="divider">|</span>OFFICE</p>
      <p class="availability">24 HOUR - ALL SUBURBS</p>

      <ul class="credentials">
        <li><svg class="tick" viewBox="0 0 40 36" aria-hidden="true"><path d="M3 20 L10 14 L16 22 L34 3 L38 7 L16 33 Z" fill="var(--tick-grey)"/></svg>Qualified tradesmen</li>
        <li><svg class="tick" viewBox="0 0 40 36" aria-hidden="true"><path d="M3 20 L10 14 L16 22 L34 3 L38 7 L16 33 Z" fill="var(--tick-grey)"/></svg>All Work Guaranteed</li>
        <li><svg class="tick" viewBox="0 0 40 36" aria-hidden="true"><path d="M3 20 L10 14 L16 22 L34 3 L38 7 L16 33 Z" fill="var(--tick-grey)"/></svg>37 Years Experience</li>
        <li><svg class="tick" viewBox="0 0 40 36" aria-hidden="true"><path d="M3 20 L10 14 L16 22 L34 3 L38 7 L16 33 Z" fill="var(--tick-grey)"/></svg>Licensed Repairer</li>
      </ul>

      <p class="brand-name">Steadfast Glass</p>
    </section>

    <p class="call-to-action">CALL 9372 6148</p>
  </main>
</body>
</html>
```